Tervolan Pty Ltd professional business card

A professional business card template using the colours from the supplied logo.
Clean crisp lines while, Modern while not being over the top.

Target Market(s)

Construction, commerical and industrial

Industry/Entity Type

Communications

Contact Information for Business Card

For a Communications, IT, Optical fibre installation company

Colors
37b8a4

```html
<!DOCTYPE html>
<html lang="en">
<head>
<meta charset="UTF-8">
<title>Tervolan Pty Ltd – Business Card</title>
<link href="https://fonts.googleapis.com/css2?family=Poppins:wght@400;500;600&display=swap" rel="stylesheet">
<style>
  :root {
    --backdrop: #d4d4d4;
    --paper: #ffffff;
    --brand-teal: #1e929f;
    --ink-grey: #6d6e71;
    --ink-dark: #333333;
    --ink-light: #ffffff;
  }
  * { margin: 0; padding: 0; box-sizing: border-box; }
  html, body {
    width: 1200px;
    height: 1000px;
    overflow: hidden;
    background: var(--backdrop);
    font-family: "Poppins", sans-serif;
  }
  .canvas {
    position: relative;
    width: 1200px;
    height: 1000px;
  }
  .card {
    position: absolute;
    left: 216px;
    width: 768px;
    height: 438px;
  }
  .card--front { top: 50px; background: var(--paper); }
  .card--back { top: 511px; background: var(--brand-teal); }

  .wordmark {
    position: absolute;
    display: flex;
    align-items: center;
    gap: 12px;
    font-weight: 500;
    letter-spacing: 0.5px;
    line-height: 1;
    white-space: nowrap;
  }
  .wordmark__dot {
    border-radius: 50%;
    flex: none;
  }
  .card--front .wordmark {
    left: 84px;
    top: 208px;
    font-size: 56px;
    color: var(--ink-grey);
  }
  .card--front .wordmark__dot {
    width: 22px; height: 22px;
    background: var(--brand-teal);
  }
  .card--back .wordmark {
    left: 50%;
    top: 180px;
    transform: translateX(-50%);
    font-size: 70px;
    color: var(--ink-light);
  }
  .card--back .wordmark__dot {
    width: 26px; height: 26px;
    background: var(--ink-light);
  }

  .holder {
    position: absolute;
    left: 448px;
    top: 116px;
  }
  .holder__name {
    font-size: 30px;
    font-weight: 500;
    color: var(--brand-teal);
    line-height: 1.2;
  }
  .holder__role {
    font-size: 17px;
    color: var(--ink-dark);
    line-height: 1.3;
  }
  .contact {
    list-style: none;
    margin-top: 42px;
    font-size: 17px;
    color: var(--ink-dark);
    line-height: 26.5px;
  }

  .back-footer {
    position: absolute;
    left: 0; right: 0;
    top: 386px;
    text-align: center;
    font-size: 17px;
    color: var(--ink-light);
    word-spacing: 1px;
  }
</style>
</head>
<body>
<main class="canvas">
  <section class="card card--front" aria-label="Business card front">
    <div class="wordmark">
      <span class="wordmark__dot"></span>
      <span class="wordmark__name">Tervolan</span>
    </div>
    <div class="holder">
      <h1 class="holder__name">MARCUS HALE</h1>
      <p class="holder__role">President</p>
      <ul class="contact">
        <li>48 Harbour Lane</li>
        <li>(615) 555-0142</li>
        <li>hello@tervolan.com</li>
        <li>www.tervolan.com</li>
      </ul>
    </div>
  </section>

  <section class="card card--back" aria-label="Business card back">
    <div class="wordmark">
      <span class="wordmark__dot"></span>
      <span class="wordmark__name">Tervolan</span>
    </div>
    <p class="back-footer">48 Harbour Lane 48 Harbour Lane</p>
  </section>
</main>
</body>
</html>
```